Tidecrest NZ Brand, Revenue, Promotions & Events

I need an innovative business card that pops my brand. I like the colours against darker gradients and i'm not afraid to be bold.

I run my own Business, Brand, Event & Promotion company. I specialise in breathing life into businesses and adding atmosphere to promotions and events. I am concept based lady that likes to test the boundaries and create stand out campaigns that connect with the consumer.

I have 12 years business experience in a realm of interesting fields form 11 years in coordinating international music festivals & promotions, 6 years in radio with 8 radio awards including a NZ radio award for best sales team in NZ and was the national brand and sales manager for New Zealands 1st indoor entertainment mall. With 10 years of experience in advertising sales, I have an eye for creating revenue streams for businesses and thrive on implementing campaigns that compliment those streams.

I love sayings like "Do what you love, love what you do" and believe that you can achieve anything you want.

I have been fortunate in my career that my connections have carried me without needing to promote my business however it is important that I start to do so.

Target Market(s)

Decision makers 25 to 54

Contact Information for Business Card

Petra Ollingham
Director
p. 022 587 3091
e. petra@tidecrest.nz
www.tidecrest.nz

FB, IG and Linkedin logo

Font styles to use
Sans Serif

Colors

Designer to choose colors to be used in the design.

Requirements
Must have
• Petra Ollingham
• Director
• p. 022 587 3091
• e. petra@tidecrest.nz
• www.tidecrest.nz
• FB, IG and Linkedin logo
Nice to have
• I am looking for a business card with character, that leaves my presence with my customer and makes them remember my brand & optimistic personality when i walk out the door.

```html
<!DOCTYPE html>
<html lang="en">
<head>
<meta charset="utf-8">
<title>Tidecrest NZ – Business Card</title>
<link rel="stylesheet" href="https://fonts.googleapis.com/css2?family=Montserrat:ital,wght@0,400;0,600;0,700;1,400&family=Arimo:wght@400&display=swap">
<style>
  :root {
    --page-bg: #ffffff;
    --navy-deep: #0e0b4a;
    --navy-mid: #132a6e;
    --ocean-blue: #1e5f9d;
    --brand-cyan: #29abe2;
    --tag-grey: #b3b3b3;
    --ink: #111111;
    --white: #ffffff;
  }
  html, body {
    margin: 0;
    width: 1200px;
    height: 1200px;
    overflow: hidden;
    background: var(--page-bg);
  }
  .sheet {
    position: relative;
    width: 1200px;
    height: 1200px;
  }
  .card {
    position: absolute;
    left: 169px;
    width: 870px;
    height: 497px;
    border-radius: 32px;
    box-shadow: 0 4px 14px rgba(0,0,0,0.35);
    overflow: hidden;
  }
  .card--front {
    top: 89px;
    background: linear-gradient(90deg, var(--navy-deep) 0%, var(--navy-deep) 40%, var(--navy-mid) 70%, var(--ocean-blue) 100%);
  }
  .card--back {
    top: 621px;
    background: var(--white);
  }
  .wordmark {
    position: absolute;
    margin: 0;
    font-family: "Montserrat", sans-serif;
    font-weight: 600;
    font-size: 62px;
    line-height: 1;
    letter-spacing: 2px;
    white-space: nowrap;
  }
  .tagline {
    position: absolute;
    margin: 0;
    font-family: "Arimo", sans-serif;
    font-size: 22.5px;
    line-height: 1;
    white-space: nowrap;
  }
  .card--front .wordmark { left: 70px; top: 196px; color: var(--white); }
  .card--front .tagline { left: 70px; top: 275px; color: var(--white); }
  .card--back .wordmark { left: 162px; top: 64px; color: var(--brand-cyan); }
  .card--back .tagline { left: 162px; top: 133px; color: var(--tag-grey); }

  .person {
    position: absolute;
    right: 483px;
    top: 260px;
    text-align: right;
    font-family: "Montserrat", sans-serif;
  }
  .person__name {
    margin: 0;
    font-weight: 700;
    font-size: 32px;
    line-height: 1;
    color: var(--ink);
    white-space: nowrap;
  }
  .person__role {
    margin: 4px 0 0;
    font-style: italic;
    font-weight: 400;
    font-size: 22px;
    line-height: 1;
    color: var(--brand-cyan);
  }
  .divider {
    position: absolute;
    left: 433px;
    top: 199px;
    width: 4px;
    height: 169px;
    border-radius: 2px;
    background: var(--brand-cyan);
  }
  .contacts {
    position: absolute;
    left: 481px;
    top: 229px;
    margin: 0;
    padding: 0;
    list-style: none;
    font-family: "Montserrat", sans-serif;
  }
  .contacts__item {
    display: flex;
    align-items: center;
    height: 32px;
    margin-bottom: 15px;
    font-size: 23px;
    color: var(--ink);
    white-space: nowrap;
  }
  .contacts__icon {
    width: 32px;
    height: 32px;
    margin-right: 22px;
    flex: none;
  }
  .socials {
    position: absolute;
    left: 377px;
    top: 429px;
    display: flex;
    gap: 16px;
  }
  .socials__dot {
    width: 29px;
    height: 29px;
    border-radius: 50%;
    background: var(--brand-cyan);
  }
</style>
</head>
<body>
<main class="sheet">
  <section class="card card--front" aria-label="Card front">
    <h1 class="wordmark">TIDECREST NZ</h1>
    <p class="tagline">BRAND | REVENUE | EVENTS &amp; PROMOTIONS</p>
  </section>

  <section class="card card--back" aria-label="Card back">
    <h2 class="wordmark">TIDECREST NZ</h2>
    <p class="tagline">BRAND | REVENUE | EVENTS &amp; PROMOTIONS</p>

    <div class="person">
      <p class="person__name">Petra Ollingham</p>
      <p class="person__role">Director</p>
    </div>

    <div class="divider"></div>

    <ul class="contacts">
      <li class="contacts__item">
        <svg class="contacts__icon" viewBox="0 0 32 32" aria-hidden="true">
          <circle cx="16" cy="16" r="16" fill="var(--brand-cyan)"/>
          <path d="M11 8.5c.8-.5 1.6-.3 2 .4l1.5 2.6c.4.7.2 1.4-.4 1.8l-1 .7c.6 1.8 2.2 3.7 4 4.6l.8-.9c.5-.6 1.3-.7 1.9-.2l2.4 1.8c.6.5.7 1.3.2 2l-1 1.2c-.8.9-2.2 1.2-3.5.6-3.7-1.6-6.6-4.8-7.9-8.6-.5-1.4-.2-2.9.8-3.7z" fill="var(--white)"/>
        </svg>
        022 587 3091
      </li>
      <li class="contacts__item">
        <svg class="contacts__icon" viewBox="0 0 32 32" aria-hidden="true">
          <circle cx="16" cy="16" r="16" fill="var(--brand-cyan)"/>
          <rect x="8" y="10.5" width="16" height="11" fill="none" stroke="var(--white)" stroke-width="1.3"/>
          <path d="M8 10.5l8 6.5 8-6.5M8 21.5l6-5.5M24 21.5l-6-5.5" fill="none" stroke="var(--white)" stroke-width="1.3"/>
        </svg>
        petra@tidecrest.nz
      </li>
      <li class="contacts__item">
        <svg class="contacts__icon" viewBox="0 0 32 32" aria-hidden="true">
          <circle cx="16" cy="16" r="16" fill="var(--brand-cyan)"/>
          <g fill="none" stroke="var(--white)" stroke-width="1.3">
            <circle cx="16" cy="16" r="9"/>
            <ellipse cx="16" cy="16" rx="4" ry="9"/>
            <path d="M7 16h18M8.2 11.5h15.6M8.2 20.5h15.6M16 7v18"/>
          </g>
        </svg>
        www.tidecrest.nz
      </li>
    </ul>

    <div class="socials">
      <span class="socials__dot" role="img" aria-label="Professional network profile"></span>
      <span class="socials__dot" role="img" aria-label="Photo sharing profile"></span>
      <span class="socials__dot" role="img" aria-label="Social network page"></span>
    </div>
  </section>
</main>
</body>
</html>
```